依頼詳細
【コンテンツ】
基本的なコンテンツは、現在のページ https://korvane.jp/ を元に構成してください。
・[制作実績] ですが、[制作実績 - ホームページ] と [制作実績 - システム開発] に分けて頂き、それぞれ簡単な説明テキスト「○○○…」とイメージ画像などがあると良いかもしれません(ブロック内の正方形のサンプル画像はそのままご使用頂いても [No Photo] 等で代替して頂いても結構です)。
・[お知らせ] と [お問い合わせはこちら] の間に [よくあるご質問] のブロックを追加してください(テキストは「○○○…」で結構です)。
・その他、企業サイトによくあるようなコンテンツで おすすめのコンテンツがございましたら デザイン内にてご提案頂けますと幸いです。

【レイアウト】
・レイアウトは(現状2カラムになってますが)1カラムで構成して頂いても結構です。おすすめのレイアウトでお願いいたします(バナー広告は不要です)。
・幅は1366pxでお願いいたします(最近見かけます画面一杯に広がっているレイアウトはあまり好みではありません。背景画像が画面一杯に広がっているのは構いませんが、コンテンツは中央よりに配置したいと思います。後ほど弊社にてレスポンシブにコーディングする予定です)。
・グローバルメニューは現状の6メニューでお願いいたします。フッターメニューは常時差し替えが発生しますので「○○○」などで代替して頂いて結構です。

【配色・デザイン等】
・配色としては モノトーン(黒)を基調として頂き、見出し背景色などもモノトーンでも結構ですし、あえて一色挙げるとしますと #405080 (HSV 225度 - 50% -50%) などのネイビーまたは青などのクールな色味が好みです。その他のアイキャッチ画像やコンテンツ等の色味は単色でもカラフルなものでも結構です。ブリッカー様のセンスにお任せしたいと思います。
・ロゴマークは先日 Brikka で依頼したものですので、変更せずにそのままご使用ください。
・アイキャッチ等の写真画像は、弊社で Pelmora Images をライセンス契約しておりますので、Pelmora Images のサンプル画像をご使用頂き、別途 画像のURLを当選後にお知らせ頂けましたら結構です。
・アイキャッチ画像のイメージ(内容)ですが、弊社のサービスは 主軸サービス(バックエンド)として (1)システム開発 があり、集客用サービス(フロントエンド)として (2)ホームページ制作 があります。これらのサービスを総合すると (1) を構成する お客様の「笑顔」と弊社の「誠実さ」との「信頼関係」(人間性)がベースとなり、その上に (2) のホームページ制作(デジタルITサービス)が存在する…といったイメージになると思います。それら2つを、例えば半透明にして手前と奥で重ね合わせる/上下にレイアウトする/2枚の画像を JavaScript でアニメーション化するなどは、ブリッカー様のセンスにてお願いできましたらと思います(弊社にてコーディングしますのでご提案ください)。
サイトURL
https://korvane.jp/
ページ数
1ページ
希望イメージ
シンプル 複雑
単色 カラフル
暗い 明るい
日常 高級
遊び心 厳粛
未来的 伝統的
女性的 男性的
希望する色
青系、水色系、グレー系
納品ファイル
• フォトショップ形式 (.psd)
補足説明
Adobe Photoshop CC *psd 形式で、レイヤーを分けて制作・納品頂けますと幸いです。
予想していたよりも提案件数が少なかったので、少し内容をシンプルにして 期間を延長させて頂きました。変更箇所とその他印象等は 以下の通りでございますので、何卒よろしくお願い申し上げます。

【依頼詳細の変更】
・アイキャッチ画像のイメージ(内容)ですが「パソコンで仕事をしている人の笑顔」が含まれている画像でしたらどんなものでも結構です。(すでにご提案頂いているものにつきましては修正して頂かなくても結構です)
・「How to enjoy creative work?」というテキストは入れて頂かない方が良いかと思います(そこまで重要視しておりませんので)。
・見出しテキスト(「制作実績」「お知らせ」など)は左寄せの方が好みです。
・全体の配色ですが、カラフルな感じより 白を基調としたモノトーンな感じの方が好みです。
・[お問い合わせはこちら] ですが、今後 他のページ(ランディングページ)などにも挿入していく可能性がありますので、バナーっぽく制作頂けますと有り難いです。

白を基調としたシンプルなレイアウトで、ディテールまで洗練されていたデザインでしたので 一目見て気に入って選ばせて頂きました。
テンプレートでのデザインが主流になりつつある中、テンプレートでは表現できないような個性のあるものになったのではないかと思いまして 大変満足しております。ありがとうございました。

皆様に個別に御礼メッセージをお送りすることはできませんでしたが、予想以上の大変多くのご提案をご応募頂けまして大変満足しております。本当にありがとうございました。また機会がございましたら 何卒よろしくお願い申し上げます。

```html
<!DOCTYPE html>
<html lang="ja">
<head>
<meta charset="utf-8">
<title>Korvane Design | システム開発専門デザイン会社</title>
<link rel="stylesheet" href="https://fonts.googleapis.com/css2?family=Montserrat:wght@400;600;700&family=Noto+Sans+JP:wght@400;500;700&display=swap">
<style>
:root{
  --navy:#3f4f82;
  --navy-dark:#33426f;
  --ink:#222;
  --text:#555;
  --muted:#888;
  --line:#ddd;
  --paper:#fff;
  --panel:#f2f2f2;
  --card-cap:#6b6b6b;
  --footer:#5a5a5a;
  --accent-yellow:rgba(214,196,90,.55);
}
*{margin:0;padding:0;box-sizing:border-box}
html,body{width:1200px;height:3176px;overflow:hidden}
body{background:var(--paper);color:var(--text);font-family:"Noto Sans JP",sans-serif;font-size:13px;position:relative}
.en{font-family:"Montserrat",sans-serif}

/* header */
.site-header{position:absolute;top:0;left:0;width:1200px;height:62px;background:var(--paper)}
.brand{position:absolute;left:88px;top:14px;display:flex;align-items:center;gap:10px;font-family:"Montserrat",sans-serif;font-weight:700;font-size:20px;color:var(--ink)}
.brand-mark{width:22px;height:22px;background:var(--ink)}
.header-note{position:absolute;right:88px;top:6px;font-size:9px;color:var(--muted)}
.global-nav{position:absolute;right:88px;top:18px;display:flex}
.global-nav a{display:block;width:104px;text-align:center;text-decoration:none;color:var(--ink);border-left:1px solid var(--line);padding-top:2px;height:36px;position:relative}
.global-nav a:last-child{border-right:1px solid var(--line)}
.global-nav .nav-en{font-family:"Montserrat",sans-serif;font-weight:600;font-size:11px;display:block}
.global-nav .nav-ja{font-size:8px;color:var(--muted);display:block;margin-top:2px}
.global-nav a.is-current::after{content:"";position:absolute;left:20px;right:20px;bottom:-6px;height:3px;background:var(--navy)}

/* hero */
.hero{position:absolute;top:62px;left:0;width:1200px;height:540px;overflow:hidden}
.hero-photo{position:absolute;inset:0;background:linear-gradient(100deg,#6f6f78 0%,#a9a9ae 35%,#d8d6d0 60%,#9c9a90 100%)}
.hero-shapes{position:absolute;inset:0}
.hero-ghost{position:absolute;font-family:"Montserrat",sans-serif;font-weight:700;color:rgba(255,255,255,.28);letter-spacing:2px}
.hero-ghost.top{right:120px;top:20px;font-size:56px}
.hero-ghost.bottom{right:60px;bottom:24px;font-size:96px}
.hero-copy{position:absolute;left:0;right:0;top:262px;text-align:center;font-family:"Montserrat",sans-serif;font-weight:600;font-size:34px;color:#fff;letter-spacing:1px}

/* intro */
.intro{position:absolute;top:640px;left:88px;width:1024px;text-align:center}
.intro-title{font-size:30px;font-weight:700;color:var(--ink);line-height:1.45}
.intro-title .em{color:var(--navy)}
.intro-text{margin-top:22px;font-size:11px;line-height:1.9;color:var(--text)}

/* works */
.works{position:absolute;top:912px;left:0;width:1200px;height:1056px;background:var(--navy)}
.section-head{text-align:center;color:#fff}
.section-head h2{font-family:"Montserrat",sans-serif;font-weight:700;font-size:38px;letter-spacing:2px}
.section-head p{font-size:10px;margin-top:2px;opacity:.8}
.work-block{position:absolute;left:88px;width:1024px}
.work-block.homepage{top:48px}
.work-block.development{top:560px}
.card-row{display:flex;gap:32px;margin-top:36px}
.work-card{width:232px;height:272px;background:#fff;position:relative;box-shadow:0 2px 6px rgba(0,0,0,.25)}
.work-thumb{position:absolute;left:0;top:0;width:232px;height:188px}
.work-caption{position:absolute;left:0;bottom:0;width:232px;height:84px;background:var(--card-cap);color:#fff;padding:14px 16px;font-size:11px;line-height:1.7;text-align:center}
.button{display:block;margin:28px auto 0;width:232px;height:44px;line-height:42px;text-align:center;font-size:12px;color:#fff;border:1px solid rgba(255,255,255,.8);background:var(--navy-dark);text-decoration:none}
.button.dark{color:#fff;background:var(--navy);border-color:var(--navy)}

/* news */
.news{position:absolute;top:2080px;left:88px;width:1024px;height:170px}
.news-label{position:absolute;left:0;top:0;width:192px;height:168px;background:#2b2b2b;color:#fff;display:flex;flex-direction:column;align-items:center;justify-content:center}
.news-label strong{font-family:"Montserrat",sans-serif;font-size:26px;letter-spacing:2px}
.news-label span{font-size:10px;margin-top:4px;opacity:.8}
.news-list{position:absolute;left:224px;top:4px;width:800px;list-style:none}
.news-list li{display:flex;gap:18px;height:32px;line-height:31px;border-bottom:1px dotted var(--line);font-size:11px;color:var(--text);white-space:nowrap;overflow:hidden}
.news-list time{font-family:"Montserrat",sans-serif;color:var(--ink);font-weight:600}

/* faq */
.faq{position:absolute;top:2306px;left:88px;width:1024px}
.faq .section-head{color:var(--ink)}
.faq .section-head h2{font-size:34px;color:var(--navy)}
.faq .section-head p{color:var(--muted);opacity:1}
.faq-row{display:flex;gap:32px;margin-top:30px}
.faq-item{width:232px;height:320px;background:var(--panel);border:1px solid var(--line)}
.faq-q{background:#4a4a4a;color:#fff;font-weight:700;font-size:12px;line-height:1.6;padding:14px 16px;height:92px}
.faq-a{padding:16px;font-size:11px;line-height:1.9;color:var(--text)}
.faq .button{margin-top:30px}

/* contact banner */
.footer{position:absolute;top:2872px;left:0;width:1200px;height:304px;background:var(--footer)}
.contact-banner{position:absolute;top:2800px;left:88px;width:1024px;height:132px;background:#fff;border:1px solid var(--line);box-shadow:0 2px 8px rgba(0,0,0,.15);display:flex;align-items:center}
.contact-icon{margin-left:34px;width:70px;height:52px}
.contact-text{margin-left:26px;color:var(--ink)}
.contact-text .lead{font-size:13px;font-weight:500}
.contact-text .main{font-size:30px;font-weight:700;margin-top:2px}
.contact-text .main .hl{color:var(--navy)}
.contact-button{margin-left:40px;width:200px;height:48px;line-height:48px;background:var(--navy);color:#fff;text-align:center;font-size:13px;font-weight:500;text-decoration:none}
.contact-person{position:absolute;right:26px;bottom:0;width:150px;height:128px;background:linear-gradient(180deg,#eef0f3,#c9cfd8);border-radius:75px 75px 0 0}

/* footer content */
.footer-links{position:absolute;top:92px;left:0;width:1200px;text-align:center;font-size:11px;color:#eee}
.footer-links a{color:#eee;text-decoration:none;padding:0 12px;border-right:1px solid #999}
.footer-links a:first-child{border-left:1px solid #999}
.footer-brand{position:absolute;top:150px;left:0;width:1200px;display:flex;justify-content:center;align-items:center;gap:10px;font-family:"Montserrat",sans-serif;font-weight:700;font-size:20px;color:#fff}
.footer-brand .brand-mark{background:#fff}
.copyright{position:absolute;top:246px;left:0;width:1200px;text-align:center;font-size:10px;color:#ccc}
</style>
</head>
<body>

<header class="site-header">
  <div class="brand"><span class="brand-mark"></span>Korvane Design</div>
  <p class="header-note">愛知県名古屋市のシステム開発・ホームページ制作会社</p>
  <nav class="global-nav">
    <a class="is-current" href="#"><span class="nav-en">TOP</span><span class="nav-ja">トップ</span></a>
    <a href="#"><span class="nav-en">HOMEPAGE</span><span class="nav-ja">ホームページ制作</span></a>
    <a href="#"><span class="nav-en">DEVELOPMENT</span><span class="nav-ja">システム開発</span></a>
    <a href="#"><span class="nav-en">PRICE</span><span class="nav-ja">料金</span></a>
    <a href="#"><span class="nav-en">COMPANY</span><span class="nav-ja">会社概要</span></a>
    <a href="#"><span class="nav-en">CONTACT</span><span class="nav-ja">お問合せ</span></a>
  </nav>
</header>

<section class="hero">
  <div class="hero-photo" role="img" aria-label="笑顔でパソコン作業をするビジネスパーソンと、ノートパソコンに表示されたウェブサイトの写真"></div>
  <svg class="hero-shapes" width="1200" height="540" viewBox="0 0 1200 540" aria-hidden="true">
    <polygon points="0,0 620,0 380,540 0,540" fill="rgba(63,79,130,.55)"/>
    <polygon points="1200,120 1200,540 640,540" fill="rgba(214,196,90,.5)"/>
  </svg>
  <span class="hero-ghost top">WEBSITE</span>
  <span class="hero-ghost bottom">HOMEPAGE</span>
  <p class="hero-copy">How to enjoy creative work?</p>
</section>

<section class="intro">
  <h1 class="intro-title"><span class="em">「モノ作りを楽しむ」</span>ことをミッションとした<br>システム開発専門デザイン会社です。</h1>
  <p class="intro-text">当社は名古屋市を拠点に、企業の業務システム開発とホームページ制作をワンストップでご提供しております。<br>お客様の笑顔と私たちの誠実さから生まれる信頼関係を大切に、使いやすく長く育てられる仕組みをお届けします。<br>小さなご相談から大規模なシステム構築まで、経験豊富なスタッフが丁寧にサポートいたします。</p>
</section>

<section class="works">
  <div class="work-block homepage">
    <div class="section-head"><h2>WORK-HOMEPAGE</h2><p>制作実績・ホームページ</p></div>
    <div class="card-row">
      <article class="work-card"><div class="work-thumb" role="img" aria-label="制作したホームページのスクリーンショット" style="background:linear-gradient(160deg,#f4f6f9,#b9c9de)"></div><p class="work-caption">この文章はダミーです。<br>フォントサイズ、文字量、<br>行送りを確認するためです。</p></article>
      <article class="work-card"><div class="work-thumb" role="img" aria-label="制作したホームページのスクリーンショット" style="background:linear-gradient(160deg,#eaf5e4,#9fcf7a)"></div><p class="work-caption">この文章はダミーです。<br>フォントサイズ、文字量、<br>行送りを確認するためです。</p></article>
      <article class="work-card"><div class="work-thumb" role="img" aria-label="制作したホームページのスクリーンショット" style="background:linear-gradient(160deg,#f7f7f7,#cfcfcf)"></div><p class="work-caption">この文章はダミーです。<br>フォントサイズ、文字量、<br>行送りを確認するためです。</p></article>
      <article class="work-card"><div class="work-thumb" role="img" aria-label="制作したホームページのスクリーンショット" style="background:linear-gradient(160deg,#fbeee0,#e59a55)"></div><p class="work-caption">この文章はダミーです。<br>フォントサイズ、文字量、<br>行送りを確認するためです。</p></article>
    </div>
    <a class="button" href="#">ホームページ実績一覧</a>
  </div>

  <div class="work-block development">
    <div class="section-head"><h2>WORK-DEVELOPMENT</h2><p>制作実績・システム開発</p></div>
    <div class="card-row">
      <article class="work-card"><div class="work-thumb" role="img" aria-label="サーバー機器の写真" style="background:linear-gradient(160deg,#d9dde4,#7b8596)"></div><p class="work-caption">この文章はダミーです。<br>フォントサイズ、文字量、<br>行送りを確認するためです。</p></article>
      <article class="work-card"><div class="work-thumb" role="img" aria-label="業務システム画面のスクリーンショット" style="background:linear-gradient(160deg,#f6f1ea,#d9b58a)"></div><p class="work-caption">この文章はダミーです。<br>フォントサイズ、文字量、<br>行送りを確認するためです。</p></article>
      <article class="work-card"><div class="work-thumb" role="img" aria-label="業務システム画面のスクリーンショット" style="background:linear-gradient(160deg,#f3f3f3,#c4c4c4)"></div><p class="work-caption">この文章はダミーです。<br>フォントサイズ、文字量、<br>行送りを確認するためです。</p></article>
      <article class="work-card"><div class="work-thumb" role="img" aria-label="管理画面のスクリーンショット" style="background:linear-gradient(160deg,#eef4f4,#8fb3b5)"></div><p class="work-caption">この文章はダミーです。<br>フォントサイズ、文字量、<br>行送りを確認するためです。</p></article>
    </div>
    <a class="button" href="#">システム開発実績一覧</a>
  </div>
</section>

<section class="news">
  <div class="news-label"><strong>NEWS</strong><span>お知らせ</span></div>
  <ul class="news-list">
    <li><time>2017.11.22</time>この文章はダミーです。フォントサイズ、文字量、行送りなどを確認するための仮の文章です。この文章はダミーです。</li>
    <li><time>2017.11.22</time>この文章はダミーです。フォントサイズ、文字量、行送りなどを確認するための仮の文章です。この文章はダミーです。</li>
    <li><time>2017.11.22</time>この文章はダミーです。フォントサイズ、文字量、行送りなどを確認するための仮の文章です。この文章はダミーです。</li>
    <li><time>2017.11.22</time>この文章はダミーです。フォントサイズ、文字量、行送りなどを確認するための仮の文章です。この文章はダミーです。</li>
    <li><time>2017.11.22</time>この文章はダミーです。フォントサイズ、文字量、行送りなどを確認するための仮の文章です。この文章はダミーです。</li>
  </ul>
</section>

<section class="faq">
  <div class="section-head"><h2>FAQ</h2><p>よくある質問</p></div>
  <div class="faq-row">
    <div class="faq-item"><p class="faq-q">Q. この文章はダミーです。フォントサイズ、文字量を確認しますか？</p><p class="faq-a">この文章はダミーです。フォントサイズ、文字量、行送りなどを確認するための仮の文章です。この文章はダミーです。フォントサイズ、文字量、行送りなどを確認するための仮の文章です。</p></div>
    <div class="faq-item"><p class="faq-q">Q. この文章はダミーです。フォントサイズ、文字量を確認しますか？</p><p class="faq-a">この文章はダミーです。フォントサイズ、文字量、行送りなどを確認するための仮の文章です。この文章はダミーです。フォントサイズ、文字量、行送りなどを確認するための仮の文章です。</p></div>
    <div class="faq-item"><p class="faq-q">Q. この文章はダミーです。フォントサイズ、文字量を確認しますか？</p><p class="faq-a">この文章はダミーです。フォントサイズ、文字量、行送りなどを確認するための仮の文章です。この文章はダミーです。フォントサイズ、文字量、行送りなどを確認するための仮の文章です。</p></div>
    <div class="faq-item"><p class="faq-q">Q. この文章はダミーです。フォントサイズ、文字量を確認しますか？</p><p class="faq-a">この文章はダミーです。フォントサイズ、文字量、行送りなどを確認するための仮の文章です。この文章はダミーです。フォントサイズ、文字量、行送りなどを確認するための仮の文章です。</p></div>
  </div>
  <a class="button dark" href="#">よくある質問一覧</a>
</section>

<footer class="footer">
  <nav class="footer-links"><a href="#">リンク1</a><a href="#">リンク2</a><a href="#">リンク3</a><a href="#">リンク4</a><a href="#">リンク5</a><a href="#">リンク6</a><a href="#">リンク7</a><a href="#">リンク8</a></nav>
  <div class="footer-brand"><span class="brand-mark"></span>Korvane Design</div>
  <p class="copyright">Copyright © 1999-2017 Korvane Design Inc. All Rights Reserved.</p>
</footer>

<aside class="contact-banner">
  <svg class="contact-icon" viewBox="0 0 70 52" aria-hidden="true">
    <rect x="2" y="2" width="66" height="48" fill="none" stroke="#444" stroke-width="3"/>
    <polyline points="2,2 35,30 68,2" fill="none" stroke="#444" stroke-width="3"/>
  </svg>
  <div class="contact-text">
    <p class="lead">お見積・ご相談・ご質問はお気軽に</p>
    <p class="main"><span class="hl">お問合せ</span>はこちら</p>
  </div>
  <a class="contact-button" href="#">お問合せフォーム</a>
  <div class="contact-person" role="img" aria-label="ヘッドセットを付けたサポートスタッフの写真"></div>
</aside>

</body>
</html>
```